Online Art Gallery & Art Management Firm looking for a business card

I'm launching an online art gallery (paintings, photography, drawings, furniture, books, ...) where people can buy all types of art. It's a platform where young and unknown artists can showcase their oeuvre.

Additionally, the venture will act as my advising company for artists. I help them out with their business side of life and become their representative.

The company name: The Velvet Parlour
Logo is attached

I'm looking for something very classy and upmarket.
Updates

Reason: Logo wasn't finished yet...

The design should include the following information: - Name: Pieter Vandomme - Title: Founder - Mobile: +32 (0) 486 514 362 - E-mail: pieter@velvet-parlour.example - Website www.velvet-parlour.example I prefer the have the logo (without website) on the one side and the information on the other. Best regards Pieter

Target Market(s)

Art buyers / art dealers / artists / middle class / upmarket /

Industry/Entity Type

Artists

Colors

Designer to choose colors to be used in the design.

Requirements
Must have
• Must communicate credibility, trust and integrity
Nice to have
• Something classy, chique
Should not have
• Nothing to artistic or creative

```html
<!DOCTYPE html>
<html lang="en">
<head>
<meta charset="utf-8">
<title>The Velvet Parlour — Business Card</title>
<link rel="stylesheet" href="https://fonts.googleapis.com/css2?family=Ubuntu:wght@300;400&display=swap">
<style>
  :root {
    --backdrop: #2f2b2b;
    --front-ink: #0e1514;
    --front-glow: #18201f;
    --back-ink: #040404;
    --paper-white: #f4f4f2;
    --type-light: #f2f2f2;
    --type-muted: #d8d8d8;
    --logo-dark: #2a2a2a;
  }
  * { box-sizing: border-box; margin: 0; padding: 0; }
  html, body {
    width: 1200px;
    height: 1200px;
    overflow: hidden;
    background: var(--backdrop);
    font-family: "Ubuntu", sans-serif;
  }
  .canvas {
    position: relative;
    width: 1200px;
    height: 1200px;
  }
  .card {
    position: absolute;
    left: 200px;
    width: 800px;
    height: 457px;
    box-shadow: 0 18px 40px rgba(0,0,0,0.45);
  }
  .card--front {
    top: 113px;
    background: radial-gradient(ellipse at 50% 55%, var(--front-glow) 0%, var(--front-ink) 70%);
    display: flex;
    align-items: center;
    justify-content: center;
  }
  .wordmark {
    color: var(--type-light);
    font-weight: 300;
    font-size: 30px;
    letter-spacing: 0.22em;
    text-transform: uppercase;
    white-space: nowrap;
  }
  .card--back {
    top: 630px;
    background: var(--back-ink);
    color: var(--type-light);
  }
  .identity {
    position: absolute;
    left: 104px;
    top: 88px;
  }
  .identity__first {
    font-weight: 300;
    font-size: 46px;
    line-height: 1.1;
  }
  .identity__last {
    font-weight: 300;
    font-size: 31px;
    line-height: 1.2;
  }
  .identity__role {
    font-size: 19px;
    color: var(--type-muted);
    margin-left: 6px;
  }
  .contact {
    display: grid;
    grid-template-columns: 54px auto;
    column-gap: 16px;
    row-gap: 2px;
    margin-top: 16px;
    font-weight: 300;
    font-size: 15px;
    line-height: 1.25;
  }
  .contact__label {
    color: var(--type-muted);
    text-align: right;
  }
  .panel {
    position: absolute;
    right: 62px;
    top: 56px;
    width: 112px;
    height: 345px;
    background: var(--paper-white);
    display: flex;
    align-items: center;
    justify-content: center;
  }
  .panel .wordmark {
    color: var(--logo-dark);
    font-size: 7.5px;
    letter-spacing: 0.16em;
  }
</style>
</head>
<body>
<main class="canvas">
  <section class="card card--front" aria-label="Card front">
    <p class="wordmark">The Velvet Parlour</p>
  </section>

  <section class="card card--back" aria-label="Card back">
    <div class="identity">
      <p class="identity__first">Pieter</p>
      <p class="identity__last">Vandomme<span class="identity__role">Founder</span></p>
      <div class="contact">
        <span class="contact__label">Mobile</span><span>+32 (0) 486 514 362</span>
        <span class="contact__label">Email</span><span>pieter@velvet-parlour.example</span>
        <span></span><span>www.velvet-parlour.example</span>
      </div>
    </div>
    <div class="panel">
      <p class="wordmark">The Velvet Parlour</p>
    </div>
  </section>
</main>
</body>
</html>
```